New Business Card Design Project

Details for my new Business Card Design Project will be added soon. Like a nice simple design

Target Market(s)

Home improvement

Industry/Entity Type

Home Improvement

Contact Information for Business Card

Roofing siding gutters additions garages decks

Requirements
Must have
• Phone 5074629183
• Email morvantgc@quellmail.com

```html
<!DOCTYPE html>
<html lang="en">
<head>
<meta charset="utf-8">
<title>Dana Whitlock – Business Card</title>
<link href="https://fonts.googleapis.com/css2?family=Audiowide&family=Bebas+Neue&family=Lato:wght@400&display=swap" rel="stylesheet">
<style>
  :root {
    --backdrop: #e9e9ea;
    --card-white: #f3f3f4;
    --brand-blue: #134a93;
    --brand-red: #e31b23;
    --sky-blue: #7bbde6;
    --service-grey: #dcdcde;
    --contact-white: #ffffff;
  }
  html, body {
    margin: 0;
    width: 1200px;
    height: 900px;
    overflow: hidden;
    background: var(--backdrop);
  }
  .canvas {
    position: relative;
    width: 1200px;
    height: 900px;
  }
  .card {
    position: absolute;
    left: 100px;
    top: 165px;
    width: 1000px;
    height: 570px;
    background: var(--card-white);
    overflow: hidden;
    box-shadow: 0 10px 30px rgba(0,0,0,0.18);
  }
  .card-shapes {
    position: absolute;
    inset: 0;
  }
  .services {
    position: absolute;
    left: 34px;
    top: 30px;
    margin: 0;
    font-family: "Audiowide", sans-serif;
    color: var(--service-grey);
    line-height: 0.82;
    font-weight: 400;
  }
  .services span { display: block; }
  .services .line-1 { font-size: 100px; }
  .services .line-2 { font-size: 88px; }
  .services .line-3 { font-size: 58px; }
  .owner-name {
    position: absolute;
    left: 92px;
    top: 376px;
    margin: 0;
    font-family: "Bebas Neue", sans-serif;
    font-size: 96px;
    line-height: 1;
    font-weight: 400;
    color: var(--sky-blue);
    letter-spacing: 1px;
  }
  .contact {
    position: absolute;
    right: 48px;
    top: 460px;
    margin: 0;
    padding: 0;
    list-style: none;
    font-family: "Lato", sans-serif;
    font-size: 32px;
    color: var(--contact-white);
  }
  .contact li {
    display: flex;
    justify-content: flex-end;
    align-items: center;
    gap: 16px;
    height: 48px;
  }
  .contact-icon {
    width: 34px;
    height: 34px;
    flex: none;
  }
</style>
</head>
<body>
<div class="canvas">
  <article class="card">
    <svg class="card-shapes" viewBox="0 0 1000 570" width="1000" height="570" aria-hidden="true">
      <rect class="top-stripe" x="0" y="0" width="1000" height="20" fill="var(--brand-red)"/>
      <polygon class="accent-sky" points="640,262 690,244 1000,244 1000,262" fill="var(--sky-blue)"/>
      <polygon class="accent-red" points="560,312 620,260 1000,260 1000,312" fill="var(--brand-red)"/>
      <polygon class="base-blue" points="0,270 232,270 252,362 410,310 1000,310 1000,570 0,570" fill="var(--brand-blue)"/>
    </svg>

    <h2 class="services">
      <span class="line-1">roofing, siding</span>
      <span class="line-2">gutter, additions</span>
      <span class="line-3">handyman services</span>
    </h2>

    <h1 class="owner-name">Dana Whitlock</h1>

    <ul class="contact">
      <li class="contact-phone">
        <span>5074629183</span>
        <svg class="contact-icon" viewBox="0 0 36 36" aria-label="Phone">
          <rect width="36" height="36" rx="7" fill="var(--brand-red)"/>
          <rect x="8" y="9" width="20" height="19" rx="2" fill="none" stroke="#fff" stroke-width="2.2"/>
          <rect x="11" y="6" width="5" height="10" rx="1.5" fill="#fff"/>
          <rect x="19" y="13" width="6" height="3" fill="#fff"/>
          <rect x="19" y="19" width="2" height="2" fill="#fff"/>
          <rect x="23" y="19" width="2" height="2" fill="#fff"/>
          <rect x="19" y="23" width="2" height="2" fill="#fff"/>
          <rect x="23" y="23" width="2" height="2" fill="#fff"/>
        </svg>
      </li>
      <li class="contact-email">
        <span>morvantgc@quellmail.com</span>
        <svg class="contact-icon" viewBox="0 0 36 36" aria-label="Email">
          <rect width="36" height="36" rx="7" fill="var(--brand-red)"/>
          <text x="18" y="26" text-anchor="middle" font-family="Lato, sans-serif" font-size="24" fill="#fff">@</text>
        </svg>
      </li>
    </ul>
  </article>
</div>
</body>
</html>
```